We are a music company that specializes in Music Mixing and Mastering. We also do vocal recording and create instrumentals for various artists. Our website is 731kv.com

Target Market(s)

Musicians, Record labels, rappers, and singers

Industry/Entity Type

Artists

Contact Information for Business Card

731KV
Industry Standard Mixing & Mastering
(484) 317-2095
sales@731kv.com
731kv.com

Requirements
Must have
• contact info and twitter (@731KV)

```html
<!DOCTYPE html>
<html lang="en">
<head>
<meta charset="utf-8">
<title>731KV Business Card</title>
<link rel="stylesheet" href="https://fonts.googleapis.com/css2?family=Alfa+Slab+One&display=swap">
<style>
  :root {
    --backdrop: #d9d9db;
    --card-black: #0a0a0a;
    --card-charcoal: #3a3a3a;
    --ink-white: #ffffff;
    --ink-soft: #e6e6e6;
    --art-red: #c8392f;
    --art-teal: #2f6f78;
    --art-dark: #151515;
  }
  * { margin: 0; padding: 0; box-sizing: border-box; }
  html, body {
    width: 1200px; height: 900px; overflow: hidden;
    background: var(--backdrop);
    font-family: "Alfa Slab One", "Arial Black", serif;
    font-weight: 400;
    color: var(--ink-white);
  }
  .canvas { position: relative; width: 1200px; height: 900px; }
  .card {
    position: absolute; left: 358px; width: 484px; height: 283px;
    overflow: hidden;
  }
  .card--front { top: 127px; background: var(--card-black); }
  .card--back { top: 488px; background: var(--card-charcoal); }

  .front-artwork {
    position: absolute; inset: 0 8px 0 8px;
    background:
      radial-gradient(circle at 78% 25%, rgba(200,57,47,.85) 0 12%, transparent 22%),
      radial-gradient(circle at 18% 70%, rgba(200,57,47,.8) 0 10%, transparent 20%),
      radial-gradient(circle at 60% 85%, rgba(200,57,47,.75) 0 10%, transparent 20%),
      radial-gradient(ellipse at 40% 35%, rgba(47,111,120,.8) 0 15%, transparent 45%),
      radial-gradient(ellipse at 50% 50%, var(--art-dark) 0 55%, var(--card-black) 75%);
  }
  .front-logo {
    position: absolute; left: 0; right: 0; top: 92px;
    text-align: center; font-size: 66px; line-height: 1; letter-spacing: -1px;
  }
  .front-tagline {
    position: absolute; left: 0; right: 0; top: 170px;
    text-align: center; font-size: 13px; letter-spacing: 1px; color: var(--ink-soft);
  }
  .front-email {
    position: absolute; left: 0; right: 0; bottom: 14px;
    text-align: center; font-size: 12px; letter-spacing: 1px; color: var(--ink-soft);
  }

  .back-artwork {
    position: absolute; inset: 0;
    background:
      radial-gradient(ellipse at 45% 40%, rgba(90,60,58,.55) 0 20%, transparent 50%),
      radial-gradient(ellipse at 30% 80%, rgba(110,50,45,.4) 0 15%, transparent 40%),
      linear-gradient(160deg, #2b2b2b, #444 50%, #2e2e2e);
  }
  .site-row {
    position: absolute; left: 8px; white-space: nowrap;
    font-size: 58px; line-height: 1; letter-spacing: -1px;
  }
  .site-row .site-suffix { font-size: 16px; letter-spacing: 0; margin-left: 4px; }
  .site-row--1 { top: 18px; }
  .site-row--2 { top: 105px; }
  .site-row--3 { top: 192px; }

  .handle-list {
    position: absolute; left: 336px; top: 12px;
    list-style: none; font-size: 15px; line-height: 23.5px;
  }
  .phone {
    position: absolute; left: 452px; top: 142px;
    transform: translate(-50%, -50%) rotate(-90deg);
    white-space: nowrap; font-size: 23px; letter-spacing: 1px;
  }
</style>
</head>
<body>
<main class="canvas">
  <section class="card card--front">
    <div class="front-artwork" role="img" aria-label="Abstract shattered texture in black, teal and red"></div>
    <h1 class="front-logo">731KV</h1>
    <p class="front-tagline">Industry Standard Mixing &amp; Mastering</p>
    <p class="front-email">sales@731kv.com</p>
  </section>

  <section class="card card--back">
    <div class="back-artwork" role="img" aria-label="Faint dark abstract texture with muted red tones"></div>
    <p class="site-row site-row--1">731KV<span class="site-suffix">.com</span></p>
    <p class="site-row site-row--2">731KV<span class="site-suffix">.com</span></p>
    <p class="site-row site-row--3">731KV<span class="site-suffix">.com</span></p>
    <ul class="handle-list">
      <li>@731KV</li><li>@731KV</li><li>@731KV</li><li>@731KV</li>
      <li>@731KV</li><li>@731KV</li><li>@731KV</li><li>@731KV</li>
      <li>@731KV</li><li>@731KV</li><li>@731KV</li>
    </ul>
    <p class="phone">(484) 317-2095</p>
  </section>
</main>
</body>
</html>
```